Business Card Design Project

for a second hand vintage clothing store. shop name is The Velvet Cupboard

Cards to be double sided

The name on the card is Joanna Whitfield

Information to put on card:

The Velvet Cupboard
Joanna Whitfield (no job title)
42/871 Dunmore St, Glenwick, Sydney, NSW, 2009.
Mobile: 0412 905 261
Email: thevelvetcupboard@mailbox.com.au
Web: www.thevelvetcupboard.com.au

Target Market(s)

Women looking at vintage clothing

Industry/Entity Type

Clothing

```html
<!DOCTYPE html>
<html lang="en">
<head>
<meta charset="utf-8">
<title>The Velvet Cupboard — Business Card</title>
<link href="https://fonts.googleapis.com/css2?family=Pinyon+Script&family=Arimo:wght@400;700&display=swap" rel="stylesheet">
<style>
  :root {
    --backdrop: #1c1c1e;
    --plum: #4b1d2d;
    --plum-deep: #3e1624;
    --amber: #d98a22;
    --cream: #e9dcae;
    --text-light: #f6e6c6;
  }
  * { margin: 0; padding: 0; box-sizing: border-box; }
  html, body {
    width: 1200px; height: 984px; overflow: hidden;
    background: var(--backdrop);
    font-family: "Arimo", Arial, sans-serif;
  }
  .sheet {
    position: relative; width: 1200px; height: 984px;
    display: flex; flex-direction: column; align-items: center; justify-content: center; gap: 40px;
  }
  .card {
    position: relative; width: 760px; height: 434px;
    border-radius: 30px; overflow: hidden;
    background: var(--amber);
  }
  .card-shape { position: absolute; inset: 0; }
  .brand-name {
    position: absolute; left: 0; right: 0; text-align: center;
    font-family: "Pinyon Script", cursive; font-weight: 400;
    color: var(--cream); white-space: nowrap;
  }
  /* front */
  .card--front .brand-name { top: 125px; font-size: 70px; }
  .web-address {
    position: absolute; left: 0; right: 0; top: 368px; text-align: center;
    font-size: 25px; letter-spacing: 3px; color: var(--plum); white-space: nowrap;
  }
  .web-address strong { font-weight: 700; }
  /* back */
  .card--back .brand-name { top: 22px; font-size: 48px; }
  .holder-name {
    position: absolute; left: 140px; top: 162px;
    font-family: "Pinyon Script", cursive; font-size: 46px; color: var(--plum); white-space: nowrap;
  }
  .contact-list {
    position: absolute; left: 300px; top: 258px;
    display: grid; grid-template-columns: auto auto; column-gap: 20px; row-gap: 4px;
    font-size: 18px; line-height: 22px; white-space: nowrap;
  }
  .contact-label { text-align: right; font-weight: 700; color: var(--plum); }
  .contact-value { color: var(--text-light); }
  .postal-address {
    position: absolute; left: 48px; top: 362px;
    font-size: 17px; color: var(--plum); white-space: nowrap;
  }
  .postal-address strong { font-weight: 700; }
</style>
</head>
<body>
<main class="sheet">

  <section class="card card--back" aria-label="Card back">
    <svg class="card-shape" viewBox="0 0 760 434" aria-hidden="true">
      <path d="M0 0 H760 V118 Q560 124 395 122 L380 138 L365 122 Q180 122 0 116 Z" fill="var(--plum)"/>
      <line x1="40" y1="152" x2="720" y2="152" stroke="var(--plum)" stroke-width="1.5" stroke-dasharray="6 5"/>
      <line x1="40" y1="344" x2="720" y2="344" stroke="var(--plum)" stroke-width="1.5" stroke-dasharray="6 5"/>
    </svg>
    <div class="brand-name">The Velvet Cupboard</div>
    <div class="holder-name">Joanna Whitfield</div>
    <div class="contact-list">
      <span class="contact-label">Mobile:</span><span class="contact-value">0412 905 261</span>
      <span class="contact-label">Email:</span><span class="contact-value">thevelvetcupboard@mailbox.com.au</span>
      <span class="contact-label">Web:</span><span class="contact-value">www.thevelvetcupboard.com.au</span>
    </div>
    <div class="postal-address"><strong>Address:</strong> 42/871 Dunmore St, Glenwick, Sydney, NSW, 2009.</div>
  </section>

  <section class="card card--front" aria-label="Card front">
    <svg class="card-shape" viewBox="0 0 760 434" aria-hidden="true">
      <path d="M0 0 H760 V338 Q560 346 395 348 L380 332 L365 348 Q180 350 0 336 Z" fill="var(--plum)"/>
      <path d="M0 336 Q180 350 365 348 L380 332 L395 348 Q560 346 760 338 V344 Q560 352 395 354 L380 338 L365 354 Q180 356 0 342 Z" fill="var(--plum-deep)" opacity="0.6"/>
    </svg>
    <div class="brand-name">The Velvet Cupboard</div>
    <div class="web-address">www.<strong>thevelvetcupboard</strong>.com.au</div>
  </section>

</main>
</body>
</html>
```